Refresh of graphic design for existing website

We would like to refresh our website. Please see the attached design specifications.

Industry/Entity Type

Graphic Design

```html
<!DOCTYPE html>
<html lang="en">
<head>
<meta charset="utf-8">
<title>The Vehicle Service Institute</title>
<link href="https://fonts.googleapis.com/css2?family=Open+Sans:wght@400;600;700&display=swap" rel="stylesheet">
<style>
:root{
  --blue:#1a6fb5;
  --blue-dark:#135a95;
  --ink:#333;
  --muted:#777;
  --line:#e2e2e2;
}
*{box-sizing:border-box;margin:0;padding:0}
html,body{width:773px;height:1200px;overflow:hidden;background:#fff;font-family:"Open Sans",Arial,sans-serif;color:var(--ink)}
.page{width:773px;height:1200px;position:relative}
.header{height:100px;position:relative}
.brand{position:absolute;left:22px;top:14px}
.brand-name{font-size:44px;font-weight:700;color:var(--blue);line-height:1;display:flex;align-items:center;gap:8px}
.brand-name .dot{width:14px;height:14px;border-radius:50%;background:var(--blue)}
.brand-tag{font-size:11px;font-weight:700;color:var(--blue);margin-top:6px;letter-spacing:.3px}
.login{position:absolute;right:22px;top:22px;width:232px}
.login .fields{display:flex;gap:6px}
.login input{width:113px;height:18px;border:1px solid #ccc;font:8px "Open Sans",sans-serif;padding:2px 5px;color:#999}
.login .row{display:flex;justify-content:space-between;align-items:flex-start;margin-top:6px;font-size:7.5px;color:var(--muted);line-height:1.5}
.login button{background:var(--blue);color:#fff;border:0;font:600 9px "Open Sans",sans-serif;width:54px;height:20px}
.nav{background:var(--blue);height:22px;display:flex;padding-left:20px}
.nav a{color:#fff;font-size:8px;font-weight:600;text-decoration:none;line-height:22px;padding:0 11px;text-transform:uppercase}
.nav a.active{background:var(--blue-dark)}
.hero{position:relative;height:345px;background:linear-gradient(120deg,#5f6a72 0%,#9aa3a8 40%,#3e454b 75%,#22272b 100%)}
.hero-caption{position:absolute;left:470px;top:160px;width:250px;background:rgba(10,40,70,.78);color:#fff;font-size:10.5px;line-height:1.45;padding:14px 16px}
.dots{position:absolute;left:0;right:0;bottom:14px;display:flex;justify-content:center;gap:7px}
.dots span{width:9px;height:9px;border-radius:50%;border:1px solid #fff}
.dots span.on{background:#fff}
.columns{display:flex;gap:22px;padding:36px 22px 0}
.col{flex:1;min-width:0}
.col h2{font-size:16px;font-weight:400;color:var(--blue);margin-bottom:14px}
.col h2 b{font-weight:600}
.event{display:flex;gap:10px;padding:8px 0;border-bottom:1px solid var(--line)}
.event .tri{width:0;height:0;border-left:6px solid var(--blue);border-top:5px solid transparent;border-bottom:5px solid transparent;margin-top:3px;flex:none}
.event h3{font-size:9.5px;font-weight:700}
.event p{font-size:8px;color:var(--muted);line-height:1.5;margin-top:3px}
.news{display:flex;gap:10px;padding:7px 0;border-bottom:1px solid var(--line)}
.badge{width:30px;height:34px;background:var(--blue);color:#fff;text-align:center;flex:none}
.badge b{display:block;font-size:13px;line-height:20px}
.badge small{display:block;font-size:7px;background:var(--blue-dark);line-height:14px}
.news h3{font-size:9.5px;font-weight:700;white-space:nowrap;overflow:hidden;text-overflow:ellipsis}
.news p{font-size:7.5px;color:var(--muted);line-height:1.45;margin-top:2px}
.links{list-style:none}
.links li{font-size:8.5px;padding:5px 0 5px 14px;position:relative;border-bottom:1px solid var(--line)}
.links li::before{content:"";position:absolute;left:2px;top:8px;width:4px;height:4px;border-right:1.5px solid var(--blue);border-top:1.5px solid var(--blue);transform:rotate(45deg)}
.about{padding:40px 22px 0}
.about h2{font-size:16px;font-weight:400;color:var(--blue);margin-bottom:10px}
.about h2 b{font-weight:600}
.about p{font-size:8.5px;line-height:1.6;color:#555;margin-bottom:10px}
.footer{position:absolute;left:0;right:0;bottom:0;height:90px;background:var(--blue);color:#fff;padding:26px 22px;font-size:7.5px;line-height:2}
.footer .social{position:absolute;right:22px;top:24px;text-align:center;font-size:7.5px}
.footer .social div{display:flex;gap:10px;margin-top:6px;justify-content:center}
.footer .social span{width:12px;height:12px;border-radius:50%;background:#fff;opacity:.9}
</style>
</head>
<body>
<div class="page">
  <header class="header">
    <div class="brand">
      <div class="brand-name">VSI <span class="dot"></span></div>
      <div class="brand-tag">THE VEHICLE SERVICE INSTITUTE</div>
    </div>
    <form class="login">
      <div class="fields"><input value="E-mail" readonly><input value="Password" readonly></div>
      <div class="row"><span>Remember Me<br>Forgot Password?</span><button type="button">Login</button></div>
    </form>
  </header>
  <nav class="nav">
    <a class="active">Home</a><a>About</a><a>Membership</a><a>VSI Members</a><a>VSI Events</a><a>Data Library</a><a>Market Research</a><a>Member Files</a><a>Contact</a>
  </nav>
  <section class="hero" role="img" aria-label="Technician working on a vehicle engine in a service bay">
    <div class="hero-caption">VSI's Mission is to advance the vehicle service industry by providing technical data and open dialog between the manufacturers of transportation products, government regulators and the providers of tools, equipment and service information.</div>
    <div class="dots"><span class="on"></span><span></span><span></span><span></span><span></span></div>
  </section>
  <main class="columns">
    <div class="col">
      <h2>Industry <b>Events</b></h2>
      <div class="event"><span class="tri"></span><div><h3>Parts Expo Show</h3><p>Harbor Expo Center<br>Fairview, Ohio</p><p>03 Nov, 2015</p></div></div>
      <div class="event"><span class="tri"></span><div><h3>Motor Trade Show</h3><p>Lakeside Convention Center<br>Fairview, Ohio</p><p>03 Nov, 2015</p></div></div>
      <div class="event"><span class="tri"></span><div><h3>Winter Service Week 2015</h3><p>Automakers commit to making<br>automatic braking standard</p><p>03 Nov, 2015</p></div></div>
    </div>
    <div class="col">
      <h2>Breaking <b>News</b></h2>
      <div class="news"><div class="badge"><b>05</b><small>Jan</small></div><div><h3>Hacking it's Everlasting Concern</h3><p>Auto makers, especially the import brands, often use VSI who...</p></div></div>
      <div class="news"><div class="badge"><b>23</b><small>Dec</small></div><div><h3>Meeting the Needs of OEM Require...</h3><p>Contributed by Dana Ruiz, Senior Partner, TorqueLine LLC...</p></div></div>
      <div class="news"><div class="badge"><b>20</b><small>Nov</small></div><div><h3>Telecoms Bridge the Connectivity...</h3><p>Contributed by Dana Ruiz, Senior Partner, TorqueLine LLC...</p></div></div>
      <div class="news"><div class="badge"><b>10</b><small>Nov</small></div><div><h3>ServiceCon Builds Industry Awareness</h3><p>Contributed by Dana Ruiz, Senior Partner, TorqueLine...</p></div></div>
    </div>
    <div class="col">
      <h2>Links</h2>
      <ul class="links">
        <li>Service Data Library</li><li>VSI News Blog</li><li>VSI Member Companies</li><li>VSI's Active Participants</li><li>Investment Planning Guide</li><li>VSI Market Research Survey</li><li>Payment Center</li><li>VIN Flowchart</li><li>Issue Log</li><li>Callout Definitions</li><li>Service Forum</li>
      </ul>
    </div>
  </main>
  <section class="about">
    <h2>Advancing the Vehicle <b>Service Industry since 1947</b></h2>
    <p>VSI is one of the most respected trade associations in the automotive aftermarket, giving fair and equitable representation to all segments of the equipment and tool industry. The institute is an association of automotive tool and equipment manufacturers and technical information providers and training organizations.</p>
    <p>Today, VSI serves the needs of a diverse industry. Its member products range from high-tech diagnostic tools to traditional hand tools. VSI membership benefits, events, and services are tailored to meet the needs of all tool and equipment makers whether manufacturers of highly technical diagnostic ranges, manufacturers or a small to mid-sized business. VSI is one of the most respected trade associations in the automotive aftermarket, giving fair and equitable representation to all segments of the equipment and tool industry. The institute is an association of automotive tool and equipment manufacturers and technical information providers and training organizations.</p>
  </section>
  <footer class="footer">
    <div>Copyright&copy;2005-2015 The Vehicle Service Institute</div>
    <div>1420 Meridian Road, Suite 310, Fairview, OH 44100 &nbsp;|&nbsp; P: 555-014-2270</div>
    <div class="social">Connect With Us<div><span></span><span></span><span></span></div></div>
  </footer>
</div>
</body>
</html>
```